yourSmileCare Brookvale Business Card

Please design a two sided business card that is Elegant and Professional
Add subtle elegant patterns to suit Spot UV printing/ or raised printing

Name: Dr Marcus T. Fenwick
Qualification: BDSc (QLD)
Title: Dental Surgeon, Clinical Director
Company: yourSmileCare Brookvale
Phone: (02) 7593 2268
Address: Shop 7/18-20 Lindon Ave Brookvale 2097
email: info@yoursmilecarebrookvale.com.au
Facebook: facebook.com/yoursmilecarebrookvale

Motto:
Quality dentistry you can trust

Description of services (not compulsory):
Preventative Dentistry | General Dentistry
Cosmetic Dentistry | Teeth Whitening
Crown and Bridge | Root Canal Therapy
Veneers | Clearvono | Orthodontics
Emergency Dental Care | After Hours

Personalised Treatment Plans
Transparent Fees

Please make sure card is elegant and professional

Target Market(s)

general population, patients,
Dental sales companies, other professions

Industry/Entity Type

Dental Clinic

Contact Information for Business Card

Name: Dr Marcus T. Fenwick
Qualification: BDSc (QLD)
Phone: (02) 7593 2268
Address: Shop 7/18-20 Lindon Ave Brookvale

Motto:

Description of services (not compulsory)

Transparent Fees

Image of dental surgery optional

Please make sure card is elegant and profession

Requirements
Must have
• Logo
• Name, Title (next to name), Business
• Phone, address, facbeook
• Must have stylish design to suit SPOT UV reflective printing
Nice to have
• Subtle elegant patterns which will have Spot UV on them when printed
• Colours to match logo colour
• Description of services
Should not have
• Small fonts that are hard to read
• DO NOT PUT IMAGES OF DENTAL INSTRUMENTS OR TEETH PLEASE

```html
<!DOCTYPE html>
<html lang="en">
<head>
<meta charset="utf-8">
<title>yourSmileCare Brookvale Business Card</title>
<link rel="stylesheet" href="https://fonts.googleapis.com/css2?family=PT+Sans:ital,wght@0,400;0,700;1,400;1,700&display=swap">
<style>
  :root {
    --backdrop: #9a9a9a;
    --paper: #f3f3f1;
    --brand-green: #76ab3a;
    --deep-green: #6a9e31;
    --ink-grey: #5d5e60;
    --rule-grey: #8c8c8c;
    --tint: rgba(118, 171, 58, 0.09);
    --white: #ffffff;
    --white-soft: rgba(255, 255, 255, 0.88);
  }
  * { margin: 0; padding: 0; box-sizing: border-box; }
  html, body { width: 1105px; height: 1200px; overflow: hidden; }
  body {
    background: var(--backdrop);
    font-family: "PT Sans", Arial, sans-serif;
    position: relative;
  }
  .card {
    position: absolute;
    left: 172px;
    width: 760px;
    height: 430px;
    overflow: hidden;
  }
  /* ---------- front ---------- */
  .card-front { top: 140px; background: var(--paper); }
  .front-motif {
    position: absolute; left: 110px; top: 10px;
    width: 140px; height: 140px; border-radius: 50%;
    background: var(--tint);
  }
  .brand-lockup {
    position: absolute; right: 32px; top: 100px;
    text-align: right; color: var(--brand-green);
    font-weight: 400; line-height: 1;
  }
  .brand-lockup .brand-name { display: block; font-size: 50px; letter-spacing: -0.5px; }
  .brand-lockup .brand-place { display: block; font-size: 32px; margin-top: 4px; letter-spacing: 1px; }
  .person {
    position: absolute; left: 34px; top: 212px; right: 32px;
  }
  .person-name { color: var(--brand-green); font-weight: 700; font-size: 28px; }
  .person-name .qualification { font-size: 19px; font-weight: 400; }
  .person-title {
    display: flex; align-items: flex-end; gap: 4px;
    color: var(--ink-grey); font-size: 20px; margin-top: 6px;
  }
  .person-title .rule { flex: 1; border-bottom: 1.5px solid var(--rule-grey); margin-bottom: 5px; }
  .contact-list {
    position: absolute; left: 34px; top: 302px; list-style: none;
    color: var(--ink-grey); font-size: 19px; line-height: 30px;
  }
  .contact-list li { display: flex; align-items: center; gap: 12px; }
  .contact-list svg { width: 18px; height: 18px; flex: none; }
  .clinic-address {
    position: absolute; right: 32px; top: 302px; text-align: right;
    color: var(--ink-grey); font-size: 19px; line-height: 30px; font-style: normal;
  }
  .clinic-address strong { color: #3f4042; }
  .front-rule { position: absolute; left: 0; right: 0; bottom: 18px; height: 3px; background: var(--rule-grey); }
  .front-band { position: absolute; left: 0; right: 0; bottom: 0; height: 15px; background: var(--brand-green); }
  /* ---------- back ---------- */
  .card-back { top: 630px; background: var(--brand-green); color: var(--white); }
  .back-motif {
    position: absolute; left: 278px; top: 28px;
    width: 84px; height: 84px; border-radius: 50%;
    background: rgba(255, 255, 255, 0.12);
  }
  .back-brand {
    position: absolute; left: 40px; top: 184px; width: 380px;
    text-align: right; color: var(--white); font-weight: 400; line-height: 1;
  }
  .back-brand .brand-name { display: block; font-size: 50px; letter-spacing: -0.5px; }
  .back-brand .brand-place { display: block; font-size: 32px; margin-top: 4px; letter-spacing: 1px; }
  .back-taglines {
    position: absolute; left: 40px; top: 282px; width: 380px;
    text-align: right; font-weight: 700; font-style: italic;
  }
  .back-taglines .motto { font-size: 22px; }
  .back-taglines .promise { font-size: 21px; line-height: 30px; margin-top: 8px; padding-right: 6px; }
  .services { position: absolute; left: 442px; top: 28px; }
  .services h2 { font-size: 23px; font-weight: 700; margin-bottom: 8px; }
  .services ul { list-style: none; font-style: italic; font-size: 20px; line-height: 29px; color: var(--white-soft); }
  .services li { padding-left: 28px; position: relative; }
  .services li::before {
    content: ""; position: absolute; left: 10px; top: 13px;
    width: 5px; height: 5px; border-radius: 50%; background: var(--white-soft);
  }
</style>
</head>
<body>

<section class="card card-front" aria-label="Business card front">
  <div class="front-motif" aria-hidden="true"></div>

  <div class="brand-lockup">
    <span class="brand-name">yourSmileCare</span>
    <span class="brand-place">Brookvale</span>
  </div>

  <div class="person">
    <p class="person-name">Dr Marcus T. Fenwick <span class="qualification">BDSc (QLD)</span></p>
    <p class="person-title"><span>Dental Surgeon, Clinical Director</span><span class="rule"></span></p>
  </div>

  <ul class="contact-list">
    <li>
      <svg viewBox="0 0 24 24" aria-hidden="true"><path fill="var(--brand-green)" d="M6.6 10.8a15.1 15.1 0 0 0 6.6 6.6l2.2-2.2a1 1 0 0 1 1-.25 11.4 11.4 0 0 0 3.6.57 1 1 0 0 1 1 1V20a1 1 0 0 1-1 1A17 17 0 0 1 3 4a1 1 0 0 1 1-1h3.5a1 1 0 0 1 1 1c0 1.25.2 2.45.57 3.57a1 1 0 0 1-.25 1z"/></svg>
      (02) 7593 2268
    </li>
    <li>
      <svg viewBox="0 0 24 24" aria-hidden="true"><rect x="2" y="5" width="20" height="14" rx="1.5" fill="var(--brand-green)"/><path d="M3 6.5l9 6.5 9-6.5" fill="none" stroke="var(--paper)" stroke-width="1.6"/></svg>
      info@yoursmilecarebrookvale.com.au
    </li>
    <li>
      <svg viewBox="0 0 24 24" aria-hidden="true"><rect x="3" y="3" width="18" height="18" fill="var(--brand-green)"/></svg>
      /yoursmilecarebrookvale
    </li>
  </ul>

  <address class="clinic-address">
    <strong>yourSmileCare Brookvale</strong><br>
    Shop 7/18-20<br>
    Lindon Ave Brookvale
  </address>

  <div class="front-rule"></div>
  <div class="front-band"></div>
</section>

<section class="card card-back" aria-label="Business card back">
  <div class="back-motif" aria-hidden="true"></div>

  <div class="back-brand">
    <span class="brand-name">yourSmileCare</span>
    <span class="brand-place">Brookvale</span>
  </div>

  <div class="back-taglines">
    <p class="motto">Quality dentistry you can trust</p>
    <p class="promise">Personalised Treatment Plans<br>Transparent Fees</p>
  </div>

  <div class="services">
    <h2>Description of Services</h2>
    <ul>
      <li>Preventative Dentistry</li>
      <li>General Dentistry</li>
      <li>Cosmetic Dentistry</li>
      <li>Teeth Whitening</li>
      <li>Crown and Bridge</li>
      <li>Root Canal Therapy</li>
      <li>Veneers</li>
      <li>Clearvono</li>
      <li>Orthodontics</li>
      <li>Emergency Dental Care</li>
      <li>After Hours</li>
    </ul>
  </div>
</section>

</body>
</html>
```